Varodel ApS cool new identity on web
Free your mind for the perfect look
Information Technology
www.varodel-example.dk
Varodel offers hosted technologies, and is one of the frontrunners and cutting edge partners for companies within webservices, and security solutions for network solutions.
1. website standard informations site, front website or other standard information sites regarding services or the company
2. website sample with eg. contact form or other types of forms, or a standard site with integrated form to contact, download information etc..
3. product login / portal site, eg. portal where clients login to on central portal with option to choose wich service they want to edit or adapt changes to - eg. our video or postsift systems with options to release mails, upload videos etc..
green
white and sand
top
www.brakvinhost.example
www.olafkestrup.example
www.qev.example
We want the design to show trust, technology, to be frontrunner, inovation etc. - streamlined with a crisp look.
Visual effects etc. are welcome to assist text, function, design and visuality.
Other website design that look interesting - however we don´t want a standard template - it´s important that we don´t look like "the others"
http://www.layoutpantry.example/website-templates/19964.html
http://www.layoutpantry.example/website-templates/19207.html
http://www.layoutpantry.example/website-templates/35125.html
http://www.layoutpantry.example/website-templates/35287.html
http://www.layoutpantry.example/website-templates/35041.html
http://www.layoutpantry.example/website-templates/34857.html
Draft of our selected stationary etc
List interface

```html
<!DOCTYPE html>
<html lang="en">
<head>
<meta charset="utf-8">
<title>Varodel ApS</title>
<link rel="stylesheet" href="https://fonts.googleapis.com/css2?family=Arimo:wght@400;700&family=Questrial&display=swap">
<style>
  :root{
    --bg-top:#2c2c2c;
    --bg-bottom:#3a3b3b;
    --green:#8cc63f;
    --green-dark:#5e9a1c;
    --orange:#f7941d;
    --gold:#e8b923;
    --link:#3ea6e0;
    --text-grey:#9a9a9a;
    --frame:#d6d6d6;
    --panel-dark:#151515;
    --white:#ffffff;
    --logo-grey:#9b9b9b;
  }
  *{box-sizing:border-box;margin:0;padding:0}
  html,body{width:1200px;height:835px;overflow:hidden}
  body{
    position:relative;
    font-family:"Arimo",Arial,sans-serif;
    background:linear-gradient(180deg,var(--bg-top) 0,#262626 492px,var(--bg-bottom) 492px,#333434 835px);
    color:var(--text-grey);
  }
  .brand{position:absolute;left:140px;top:38px;display:flex;align-items:center;gap:18px}
  .brand-mark{width:52px;height:52px;background:var(--green);border-radius:6px}
  .brand-name{font-weight:700;font-size:66px;color:var(--logo-grey);letter-spacing:1px}
  .corner-ribbons{position:absolute;right:0;top:0}

  .slider{position:absolute;left:132px;top:144px;width:924px;height:295px;background:var(--frame);border-radius:10px;padding:10px}
  .slide{position:relative;height:200px;border-radius:6px;overflow:hidden;
    background:radial-gradient(ellipse at 45% 100%,#2f5a18 0,#111 55%,var(--panel-dark) 100%)}
  .slide-media{position:absolute;left:72px;top:38px;width:384px;height:168px;border:3px solid #cfd8e0;
    background:linear-gradient(180deg,#e9eef3 0,#5b86a8 45%,#1f3f63 100%)}
  .slide-copy{position:absolute;left:492px;top:30px;width:400px;color:var(--white)}
  .slide-title{font-size:27px;line-height:32px;font-weight:400}
  .slide-text{margin-top:12px;font-size:11px;line-height:15px;color:#d8d8d8}
  .slider-arrow{position:absolute;top:95px;width:0;height:0;border-top:11px solid transparent;border-bottom:11px solid transparent}
  .slider-arrow.prev{left:-52px;border-right:13px solid var(--link)}
  .slider-arrow.next{right:-52px;border-left:13px solid var(--link)}
  .thumbs{display:flex;gap:20px;padding:18px 26px 0}
  .thumb{width:64px;height:52px;border:2px solid #fff;box-shadow:0 1px 3px rgba(0,0,0,.5)}

  .main-nav{position:absolute;left:132px;top:463px;display:flex;gap:4px}
  .main-nav a{display:block;height:29px;padding:0 16px;line-height:30px;font-size:12px;font-weight:700;color:#1d2d0c;
    text-decoration:none;background:linear-gradient(180deg,#b5e06a,var(--green));border-radius:5px 5px 0 0}
  .nav-rule{position:absolute;left:0;top:490px;width:1200px;height:4px;background:var(--green)}

  .col{position:absolute;top:506px}
  .col-title{font-family:"Questrial",sans-serif;font-size:30px;color:var(--orange);font-weight:400}
  .col-divider{position:absolute;top:506px;width:1px;height:300px;background:#555}
  .feature-img{margin-top:8px;height:92px;border:4px solid var(--gold)}
  .who{left:132px;width:236px}
  .who .feature-img{background:linear-gradient(135deg,#f2f2f2,#bfc6cc)}
  .lead-link{display:block;margin-top:13px;color:var(--link);font-size:13px;text-decoration:none}
  .col p{margin-top:3px;font-size:12px;line-height:14px;color:var(--text-grey)}
  .read-more{display:block;margin-top:10px;color:var(--link);font-size:14px;text-decoration:none}
  .what{left:444px;width:262px}
  .what .feature-img{width:252px;border-color:#d0d0d0;background:linear-gradient(135deg,#e7e7e7,#b63a3a 60%,#8e1e1e)}
  .service-list{list-style:none;margin-top:12px}
  .service-list li{height:16px;margin-bottom:4px;padding-left:12px;font-size:10px;line-height:16px;color:#333;
    background:linear-gradient(90deg,var(--gold) 0 6px,#f0f0f0 6px);border-radius:3px}
  .login{left:787px;width:284px}
  .login label{display:block;margin-top:8px;font-size:12px;color:var(--white)}
  .field{margin-top:4px;width:276px;height:29px;background:#1e1e1e;border:1px solid #555}
  .login-row{display:flex;justify-content:space-between;margin-top:6px}
  .remember{font-size:10px;color:#ccc;display:flex;align-items:center;gap:5px}
  .remember span.box{width:9px;height:9px;background:#fff}
  .forgot{display:block;margin-top:3px;font-size:10px;color:var(--link)}
  .submit{width:60px;height:24px;background:linear-gradient(180deg,#aaa,#777);color:#eee;font-size:10px;line-height:24px;text-align:center;border-radius:2px}

  .legal{position:absolute;left:132px;top:774px;font-size:11px;color:#777}
  .social{position:absolute;left:468px;top:768px;display:flex;gap:22px}
  .social span{width:32px;height:32px;border-radius:50%;background:#6a6a6a}
  .contact{position:absolute;left:787px;top:770px;font-size:11px;line-height:16px;color:#6f6f6f;display:grid;grid-template-columns:150px 150px}
</style>
</head>
<body>
  <header class="brand">
    <span class="brand-mark"></span>
    <span class="brand-name">Varodel</span>
  </header>

  <svg class="corner-ribbons" width="220" height="170" viewBox="0 0 220 170" font-family="Arimo, sans-serif" font-size="11" fill="#1d2d0c">
    <g transform="translate(40,-20) rotate(40)">
      <rect x="0" y="0" width="220" height="24" fill="#f7941d"/>
      <text x="70" y="16">Client Login</text>
      <rect x="-20" y="30" width="240" height="24" fill="#8cc63f"/>
      <text x="60" y="46">Live Support</text>
      <rect x="-40" y="60" width="260" height="24" fill="#6cb02c"/>
      <text x="50" y="76">Contact Us</text>
    </g>
  </svg>

  <section class="slider">
    <div class="slide">
      <div class="slide-media" role="img" aria-label="Website screenshot of a business service page"></div>
      <div class="slide-copy">
        <h1 class="slide-title">Lorem ipsum dolor sit amet, consectetur adipiscing elit.</h1>
        <p class="slide-text">Lorem ipsum dolor sit amet, consectetur adipiscing elit. Morbi in nisl risus. Mauris ultricies nulla vulputate augue volutpat in semper eros iaculis. Aliquam aliquet lacus bibendum lectus mattis vitae semper lacus vestibulum. Donec posuere molestie tellus, ut blandit lacus aliquet id.</p>
      </div>
    </div>
    <span class="slider-arrow prev"></span>
    <span class="slider-arrow next"></span>
    <div class="thumbs">
      <span class="thumb" role="img" aria-label="Slide preview" style="background:#3d6e96"></span>
      <span class="thumb" role="img" aria-label="Slide preview" style="background:#5a6a7a"></span>
      <span class="thumb" role="img" aria-label="Slide preview" style="background:#2a5aa8"></span>
      <span class="thumb" role="img" aria-label="Slide preview" style="background:#b04040"></span>
      <span class="thumb" role="img" aria-label="Slide preview" style="background:#6d8fa8"></span>
      <span class="thumb" role="img" aria-label="Slide preview" style="background:#4e8e3a"></span>
      <span class="thumb" role="img" aria-label="Slide preview" style="background:#2e5f8a"></span>
      <span class="thumb" role="img" aria-label="Slide preview" style="background:#8ca3b8"></span>
      <span class="thumb" role="img" aria-label="Slide preview" style="background:#345a7e"></span>
      <span class="thumb" role="img" aria-label="Slide preview" style="background:#7a8a5a"></span>
    </div>
  </section>

  <nav class="main-nav">
    <a href="#">Accessories</a><a href="#">Web Services</a><a href="#">Network</a><a href="#">Register</a><a href="#">Security</a><a href="#">Product</a>
  </nav>
  <div class="nav-rule"></div>

  <section class="col who">
    <h2 class="col-title">who we are</h2>
    <div class="feature-img" role="img" aria-label="Diagram sketch of website planning"></div>
    <a class="lead-link" href="#">Lorem ipsum dolor sit amet</a>
    <p>Consectetuer adipiscing elit. Praesent vestibulum molestie lacus. Aenean nonummy</p>
    <a class="read-more" href="#">read more</a>
  </section>
  <span class="col-divider" style="left:408px"></span>

  <section class="col what">
    <h2 class="col-title">what we do</h2>
    <div class="feature-img" role="img" aria-label="Keyboard with a red help key"></div>
    <ul class="service-list">
      <li>Consectetuer adipiscing elit. Praesent vest</li>
      <li>Molestie lacus aenean nonummy hendrerit</li>
      <li>Phasellus porta fusce suscipit varius</li>
    </ul>
    <a class="read-more" href="#">read more</a>
  </section>
  <span class="col-divider" style="left:756px"></span>

  <section class="col login">
    <h2 class="col-title">Login</h2>
    <label>Username</label>
    <div class="field"></div>
    <label>Password</label>
    <div class="field"></div>
    <div class="login-row">
      <div>
        <span class="remember"><span class="box"></span>Remember me</span>
        <a class="forgot" href="#">Forgot password?</a>
      </div>
      <span class="submit">Submit</span>
    </div>
  </section>

  <footer>
    <p class="legal">varodel.example © 2011 &nbsp;|&nbsp; Privacy Policy &nbsp;|&nbsp; Sitemap</p>
    <div class="social"><span></span><span></span><span></span><span></span><span></span></div>
    <div class="contact">
      <span>Phone: 000-222-333-0</span><span>Fax: 000-222-333-0</span>
      <span>Email: 000-222-333-0</span><span>Address: 000-222-333-0</span>
    </div>
  </footer>
</body>
</html>
```